Company Profile for Consulting Comany

Need Company profile to be designed in a professional way.

for inspiring :-
https://www.folivane.net/gallery/5372904/COMPANY-PROFILE
https://www.folivane.net/gallery/60391742/Biotech-Product-Catalog-No1-(Laminar-Air-Flow)
https://www.folivane.net/gallery/73905218/MPG-Globalpath-Company-Profile-2014-(MPG-Rebrand-part-2)

Target Market(s)

Corporate

Industry/Entity Type

It Company

Font styles to use
Sans Serif

Requirements
Must have
• Landscape A4 size
• Must go with the logo branding
• Must Have Visual Identity is the most important
• Must Have mpty spaces

```html
<!DOCTYPE html>
<html lang="en">
<head>
<meta charset="utf-8">
<title>Shift Vector – Company Profile Cover Spread</title>
<link rel="stylesheet" href="https://fonts.googleapis.com/css2?family=Open+Sans:wght@400;600&display=swap">
<style>
  :root {
    --backdrop: #d9dadc;
    --paper: #f4f4f4;
    --brand-blue: #4fc3dc;
    --ink-gray: #6b7177;
    --ink-soft: #8a9096;
    --slate-dark: #27313c;
    --slate-mid: #3c4854;
    --photo-light: #c9cbcd;
    --photo-dark: #2c2e31;
    --white: #ffffff;
  }
  * { margin: 0; padding: 0; box-sizing: border-box; }
  html, body {
    width: 1200px; height: 900px; overflow: hidden;
    background: var(--backdrop);
    font-family: "Open Sans", Arial, sans-serif;
  }
  .spread {
    position: absolute; left: 40px; top: 252px;
    width: 1120px; height: 396px;
    display: flex;
    box-shadow: 0 6px 18px rgba(0,0,0,0.18);
  }
  .page { position: relative; width: 560px; height: 396px; overflow: hidden; background: var(--paper); }

  /* Back cover */
  .back-contact {
    position: absolute; left: 14px; top: 226px; width: 180px;
    color: var(--ink-soft); font-size: 5.5px; line-height: 8px;
  }
  .back-contact h3 { color: var(--brand-blue); font-weight: 400; font-size: 8px; letter-spacing: .5px; margin-bottom: 6px; }
  .office { margin-bottom: 14px; }
  .office strong { display: block; font-weight: 600; }
  .back-visual {
    position: absolute; left: 207px; top: 0; width: 353px; height: 396px;
    background: radial-gradient(ellipse at 45% 40%, var(--slate-mid) 0%, var(--slate-dark) 70%);
  }
  .back-brand {
    position: absolute; left: 207px; top: 0; width: 353px; height: 396px;
    display: flex; align-items: center; justify-content: center; gap: 10px;
  }
  .brand-name-large { color: var(--brand-blue); font-size: 26px; font-weight: 600; letter-spacing: .5px; }
  .brand-dot-large { width: 14px; height: 14px; border-radius: 50%; background: var(--brand-blue); }

  /* Front cover */
  .front-photo {
    position: absolute; left: 312px; top: 0; width: 248px; height: 396px;
    background: linear-gradient(160deg, var(--photo-light) 0%, #8d9093 45%, var(--photo-dark) 100%);
  }
  .front-brand { position: absolute; left: 22px; top: 48px; display: flex; align-items: center; gap: 8px; }
  .brand-dot { width: 12px; height: 12px; border-radius: 50%; background: var(--brand-blue); }
  .brand-name { color: var(--brand-blue); font-size: 18px; font-weight: 600; }
  .headline-band {
    position: absolute; left: 7px; top: 166px; width: 430px; height: 96px;
    background: var(--brand-blue); color: var(--white);
    padding: 14px 0 0 22px;
  }
  .headline-band::before {
    content: ""; position: absolute; left: 14px; top: 14px; width: 1px; height: 68px;
    background: var(--ink-gray);
  }
  .headline-kicker { font-size: 11px; letter-spacing: .4px; color: var(--ink-gray); margin-bottom: 10px; }
  .headline-main { font-size: 26px; letter-spacing: .3px; font-weight: 400; }
  .service-line {
    position: absolute; left: 20px; top: 362px;
    font-size: 7px; letter-spacing: .6px; color: var(--ink-gray);
  }
</style>
</head>
<body>
  <main class="spread">
    <section class="page back-cover">
      <div class="back-contact">
        <h3>CONTACT US</h3>
        <div class="office">
          <strong>DUBAI</strong>
          PO BOX 48210, Dubai, UAE<br>
          12th Floor, Harbor Plaza Tower 1, Marina Way<br>
          T: 00971 4 555 0142<br>
          F: 00971 4 555 0143<br>
          E: info@shiftvector.com
        </div>
        <div class="office">
          <strong>KSA</strong>
          PO BOX 5521, Khobar 31952, SAUDI ARABIA<br>
          3rd Floor, Palm Gate Tower, Coastal Rd.<br>
          T: 00966 13 555 0187<br>
          E: ksa@shiftvector.com
        </div>
      </div>
      <div class="back-visual" role="img" aria-label="Blurred photo of a modern office interior in dark slate blue tones"></div>
      <div class="back-brand">
        <span class="brand-dot-large"></span>
        <span class="brand-name-large">Shift Vector</span>
      </div>
    </section>

    <section class="page front-cover">
      <div class="front-photo" role="img" aria-label="Photo of a business person in a dark suit touching a glowing network of connected nodes"></div>
      <div class="front-brand">
        <span class="brand-dot"></span>
        <span class="brand-name">Shift Vector</span>
      </div>
      <div class="headline-band">
        <p class="headline-kicker">WE CAN HELP YOU TO</p>
        <h1 class="headline-main">MAKE CHANGE HAPPEN</h1>
      </div>
      <p class="service-line">STRATEGY | PEOPLE | TECHNOLOGY</p>
    </section>
  </main>
</body>
</html>
```